Business cards, Stationery for Travel Company
Cobalt Voyages
Business cards, Stationery for Travel Company - Travel
Creative Brief
Use specific fonts
You can use what you think will look good with the logo.
Bright & Fun-filled
Anne-Claude Brovatik
Owner
24117 Hollow Creek Avenue Weston, FL 33418
anne-claude@cobaltvoyages-example.com
CobaltVoyages-example.com
I am not sure whether I want a dark card with the gold lettered logo or a white card with black lettering. I have uploaded both so that we can see the layouts in both. For the actual design, I would like a smaller version of the Cobalt Voyages logo on side one with the info above. And a larger logo on the back side. I also need to have the words "an affiliate of Red Lantern Travel" under the logo.
I would like the Cobalt Voyages logo much bigger and then the tag line underneath in a more simple font, " Mastering the Art of Travel". Then, perhaps to one side down by the bottom, I need to also add another logo for the consortium that I belong to called Meridane. I will attach that logo as well.

```html
<!DOCTYPE html>
<html lang="en">
<head>
<meta charset="utf-8">
<title>Cobalt Voyages — Stationery Set</title>
<link rel="stylesheet" href="https://fonts.googleapis.com/css2?family=Cinzel:wght@600&family=Lato:wght@400;700&display=swap">
<style>
  :root {
    --backdrop: #2d2e4b;
    --paper: #ffffff;
    --red: #a3131c;
    --red-deep: #6e0a10;
    --gold: #c9a24a;
    --ink: #3a3a3a;
    --black-card: #141212;
  }
  * { box-sizing: border-box; margin: 0; padding: 0; }
  html, body { width: 1200px; height: 811px; overflow: hidden; }
  body { background: var(--backdrop); font-family: "Lato", sans-serif; position: relative; }

  .piece { position: absolute; background: var(--paper); overflow: hidden; box-shadow: 0 6px 18px rgba(0,0,0,.35); }
  .wave { position: absolute; left: 0; width: 100%; height: 100%; top: 0; }

  .brand { position: absolute; display: flex; align-items: center; gap: 6px;
           font-family: "Cinzel", serif; font-weight: 600; color: var(--red); letter-spacing: .08em; white-space: nowrap; }
  .brand .dot { border-radius: 50%; background: var(--red); flex: none; }
  .brand.on-dark { color: var(--gold); }
  .brand.on-dark .dot { background: var(--red); border: 1px solid var(--gold); }

  .contact { position: absolute; font-size: 5.5px; line-height: 1.55; color: var(--ink); }
  .contact.light { color: #f4e9d6; }
  .contact.right { text-align: right; }

  .partner { position: absolute; display: flex; align-items: center; gap: 3px; font-size: 6px; color: var(--ink); letter-spacing: .05em; }
  .partner .sq { width: 6px; height: 6px; background: var(--ink); }
  .partner.light { color: #f4e9d6; }
  .partner.light .sq { background: #f4e9d6; }

  .seal { position: absolute; border-radius: 50%; background: radial-gradient(circle at 40% 35%, #c52a2f, var(--red-deep)); }

  /* positions */
  .envelope-back { left: 60px; top: 60px; width: 320px; height: 165px; }
  .envelope-dl   { left: 60px; top: 255px; width: 320px; height: 150px; }
  .envelope-c5   { left: 60px; top: 435px; width: 320px; height: 150px; }
  .letterhead-a  { left: 430px; top: 40px; width: 260px; height: 350px; }
  .letterhead-b  { left: 730px; top: 40px; width: 260px; height: 350px; }
  .card { position: absolute; width: 200px; height: 114px; overflow: hidden; box-shadow: 0 6px 18px rgba(0,0,0,.4); border-radius: 3px; }
  .card-black-back  { left: 440px; top: 440px; background: var(--black-card); }
  .card-black-front { left: 440px; top: 590px; background: linear-gradient(135deg, #2a1214, var(--black-card) 60%); }
  .card-white-front { left: 700px; top: 440px; background: var(--paper); }
  .card-red-back    { left: 700px; top: 590px; background: linear-gradient(135deg, #b51a22, var(--red-deep)); }

  .tagline { position: absolute; font-size: 6px; letter-spacing: .12em; color: var(--gold); white-space: nowrap; }
</style>
</head>
<body>

<!-- Envelope, back with flap and seal -->
<div class="piece envelope-back">
  <svg class="wave" viewBox="0 0 320 165" preserveAspectRatio="none">
    <polyline points="0,0 160,62 320,0" fill="none" stroke="#d9d9d9" stroke-width="1"/>
  </svg>
  <div class="seal" style="left:138px; top:40px; width:44px; height:44px;" role="img" aria-label="Red wax seal closing the envelope flap"></div>
  <div class="brand" style="left:14px; top:140px; font-size:6px;">Cobalt Voyages</div>
</div>

<!-- DL envelope, front -->
<div class="piece envelope-dl">
  <svg class="wave" viewBox="0 0 320 150" preserveAspectRatio="none">
    <path d="M0,150 L0,112 C90,70 200,20 320,30 L320,150 Z" fill="var(--red)"/>
    <path d="M0,108 C90,66 200,16 320,26" fill="none" stroke="var(--gold)" stroke-width="1.2"/>
  </svg>
  <div class="brand" style="left:14px; top:16px; font-size:9px;"><span class="dot" style="width:12px;height:12px;"></span>Cobalt Voyages</div>
  <div class="contact" style="left:14px; top:36px;">24117 Hollow Creek Avenue<br>Weston, FL 33418</div>
  <div class="partner light" style="right:14px; top:118px;"><span class="sq"></span>Meridane</div>
</div>

<!-- C5 envelope, front -->
<div class="piece envelope-c5">
  <svg class="wave" viewBox="0 0 320 150" preserveAspectRatio="none">
    <path d="M0,150 L0,78 C110,120 220,110 320,92 L320,150 Z" fill="var(--red)"/>
    <path d="M0,73 C110,115 220,105 320,87" fill="none" stroke="var(--gold)" stroke-width="1.2"/>
  </svg>
  <div class="brand" style="left:14px; top:16px; font-size:9px;"><span class="dot" style="width:12px;height:12px;"></span>Cobalt Voyages</div>
  <div class="contact" style="left:14px; top:36px;">24117 Hollow Creek Avenue<br>Weston, FL 33418</div>
  <div class="partner" style="right:14px; top:22px;"><span class="sq"></span>Meridane</div>
</div>

<!-- Letterhead, wave at foot -->
<div class="piece letterhead-a">
  <svg class="wave" viewBox="0 0 260 350" preserveAspectRatio="none">
    <path d="M0,350 L0,290 C70,320 170,300 260,262 L260,350 Z" fill="var(--red)"/>
    <path d="M0,285 C70,315 170,295 260,257" fill="none" stroke="var(--gold)" stroke-width="1.2"/>
  </svg>
  <div class="brand" style="left:50%; transform:translateX(-50%); top:22px; font-size:10px;"><span class="dot" style="width:14px;height:14px;"></span>Cobalt Voyages</div>
  <div class="contact light right" style="right:12px; top:300px;">Anne-Claude Brovatik, Owner<br>Tel (954) 555-0142<br>anne-claude@cobaltvoyages-example.com<br>CobaltVoyages-example.com</div>
</div>

<!-- Letterhead, red band at top -->
<div class="piece letterhead-b">
  <svg class="wave" viewBox="0 0 260 350" preserveAspectRatio="none">
    <path d="M120,0 L260,0 L260,78 C200,60 160,30 120,0 Z" fill="var(--red)"/>
    <path d="M112,0 C155,32 198,62 260,82" fill="none" stroke="var(--gold)" stroke-width="1.2"/>
    <path d="M0,350 L0,322 C80,340 180,330 260,312 L260,350 Z" fill="var(--red)"/>
    <path d="M0,317 C80,335 180,325 260,307" fill="none" stroke="var(--gold)" stroke-width="1"/>
  </svg>
  <div class="brand" style="left:12px; top:20px; font-size:8px;"><span class="dot" style="width:12px;height:12px;"></span>Cobalt Voyages</div>
  <div class="contact light right" style="right:10px; top:14px;">24117 Hollow Creek Avenue<br>Weston, FL 33418<br>Tel (954) 555-0142<br>CobaltVoyages-example.com</div>
</div>

<!-- Business card, black, logo side -->
<div class="card card-black-back">
  <svg class="wave" viewBox="0 0 200 114" preserveAspectRatio="none">
    <path d="M0,82 C70,70 140,92 200,70" fill="none" stroke="var(--gold)" stroke-width="1"/>
  </svg>
  <div class="brand on-dark" style="left:50%; transform:translateX(-50%); top:34px; font-size:12px;"><span class="dot" style="width:18px;height:18px;"></span>Cobalt Voyages</div>
  <div class="tagline" style="left:50%; transform:translateX(-50%); top:60px;">Mastering the Art of Travel</div>
  <div class="partner light" style="left:10px; bottom:8px;"><span class="sq"></span>Meridane</div>
</div>

<!-- Business card, black, info side -->
<div class="card card-black-front">
  <svg class="wave" viewBox="0 0 200 114" preserveAspectRatio="none">
    <path d="M0,58 C70,46 140,64 200,44" fill="none" stroke="var(--gold)" stroke-width="1"/>
  </svg>
  <div class="brand on-dark" style="left:12px; top:14px; font-size:9px;"><span class="dot" style="width:12px;height:12px;"></span>Cobalt Voyages</div>
  <div class="contact light" style="left:12px; top:66px;">Anne-Claude Brovatik, Owner<br>24117 Hollow Creek Avenue Weston, FL 33418<br>anne-claude@cobaltvoyages-example.com<br>CobaltVoyages-example.com</div>
</div>

<!-- Business card, white, info side -->
<div class="card card-white-front">
  <svg class="wave" viewBox="0 0 200 114" preserveAspectRatio="none">
    <path d="M0,114 L0,66 C70,92 140,78 200,56 L200,114 Z" fill="var(--red)"/>
    <path d="M0,61 C70,87 140,73 200,51" fill="none" stroke="var(--gold)" stroke-width="1"/>
  </svg>
  <div class="brand" style="left:12px; top:14px; font-size:9px;"><span class="dot" style="width:12px;height:12px;"></span>Cobalt Voyages</div>
  <div class="contact" style="left:12px; top:32px;">Anne-Claude Brovatik<br>Owner</div>
  <div class="contact light right" style="right:10px; top:80px;">24117 Hollow Creek Avenue Weston, FL 33418<br>anne-claude@cobaltvoyages-example.com<br>CobaltVoyages-example.com</div>
</div>

<!-- Business card, red, logo side -->
<div class="card card-red-back">
  <div class="brand on-dark" style="left:50%; transform:translateX(-50%); top:38px; font-size:12px;"><span class="dot" style="width:18px;height:18px;"></span>Cobalt Voyages</div>
  <div class="tagline" style="left:50%; transform:translateX(-50%); top:64px;">an affiliate of Red Lantern Travel</div>
  <div class="partner light" style="right:10px; bottom:8px;"><span class="sq"></span>Meridane</div>
</div>

</body>
</html>
```